Website Redesign For Motorbike Rental Company In Thailand

We are a motorbike rental start up in Phuket, Thailand named RIDE ON.

We cater to the tourist and even ex pats that want to rent a motorbike for as short as only 3 days up to 1 year at a time.

We want a website that makes it a very simple ordering process for the customer. Be able to order a motorbike rental without scrolling down...

Simple, attractive design that builds trust and credibility is huge.

Please check this google doc for the CONTENT: https://files.plomvark.example/doc/7KqW3rTzLm92XbVnPc4HsJd8FgYe0aRuNtQiMoEwZ1y/view?mode=share

Target Market(s)

Tourists In Thailand & Expats In Thailand

Industry/Entity Type

motorbike rental, motorcycle rental

Number of Pages Required

1 page

Requirements
Must have
• Must have a thailand phuket theme or feel
Nice to have
• We want a website that makes it a very simple ordering process for the customer. Be able to order a motorbike rental without scrolling down... Simple, attractive design that builds trust and credibility is huge.
Should not have
• na

```html
<!DOCTYPE html>
<html lang="en">
<head>
<meta charset="utf-8">
<title>RIDE ON – Motorbike Rentals Phuket</title>
<link href="https://fonts.googleapis.com/css2?family=Josefin+Sans:wght@400;600;700&display=swap" rel="stylesheet">
<style>
:root{
  --orange:#f07a12;
  --orange-deep:#e66f0a;
  --ink:#1c1c1c;
  --dark:#2a2a2e;
  --paper:#f6f6f6;
  --white:#ffffff;
  --gutter:#6d696b;
  --muted:#8a8a8a;
  --card-grey:#efefef;
  --card-peach:#fdeee3;
  --card-mint:#e3f6ea;
}
*{margin:0;padding:0;box-sizing:border-box}
html,body{width:929px;height:1200px;overflow:hidden}
body{position:relative;background:var(--gutter);font-family:'Josefin Sans',sans-serif;color:var(--ink)}
.a{position:absolute}
.page{position:absolute;top:0;overflow:hidden;background:var(--paper)}
.page-desktop{left:0;width:565px;height:1200px}
.page-full{left:625px;width:292px;height:1200px;background:var(--white)}
.hero{background:linear-gradient(160deg,#4a4c55 0%,#2d2f36 45%,#5a3a36 75%,#3a3c44 100%)}
.hero-shade{background:rgba(20,20,25,.35)}
.navbar{background:var(--white);display:flex;align-items:center}
.brand{display:flex;align-items:center;gap:3px;color:var(--orange);font-weight:700}
.brand-dot{border-radius:50%;background:var(--orange)}
.nav-links{display:flex}
.phone-badge{border-radius:50%;background:var(--orange);display:flex;align-items:center;justify-content:center}
.hero-title{color:var(--white);font-weight:700;text-align:center;line-height:1.15}
.btn-orange{background:var(--orange);color:var(--white);font-weight:600;display:flex;align-items:center;justify-content:center;text-transform:uppercase}
.btn-black{background:#000;color:var(--white);font-weight:600;display:flex;align-items:center;justify-content:center}
.booking{background:var(--white);box-shadow:0 2px 6px rgba(0,0,0,.08)}
.field{border:1px solid #dcdcdc;display:flex;align-items:center;color:#9a9a9a}
.flag{display:inline-block;background:linear-gradient(#c8102e 0 17%,#fff 17% 33%,#2d2a6e 33% 67%,#fff 67% 83%,#c8102e 83%)}
.sec-icon{display:flex;align-items:center;justify-content:center}
.sec-icon .line{height:1px;background:#555}
.sec-icon .dot{border-radius:50%;background:var(--orange)}
.heading{font-weight:600;text-align:center}
.illus{background:linear-gradient(135deg,#f4a35c,#d5651a 55%,#5a3a26)}
.step{overflow:hidden}
.step-num{position:absolute;right:-2px;bottom:-8px;color:var(--white);font-weight:700;line-height:1}
.photo-a{background:linear-gradient(140deg,#7aa650,#c9a37e 45%,#4a5a3a)}
.photo-b{background:linear-gradient(180deg,#9aa8b4,#6f6a66 50%,#5e5a58)}
.photo-c{background:linear-gradient(180deg,#5a6c70,#a63a3a 60%,#5a4a44)}
.features li{list-style:none;display:flex;align-items:center}
.tick-box{display:inline-block;border:1px solid var(--orange);flex:none}
.band-orange{background:linear-gradient(180deg,#f07a12,#e7720d)}
.bike-card{background:var(--white)}
.bike-photo{background:radial-gradient(ellipse at center,#6b6f78 0%,#c9ccd2 55%,#ffffff 75%)}
.bike-photo.blue{background:radial-gradient(ellipse at center,#2a6fb5 0%,#9cc0e2 55%,#ffffff 75%)}
.bike-photo.black{background:radial-gradient(ellipse at center,#2c2c30 0%,#a9abb0 55%,#ffffff 75%)}
.price{text-align:center;font-weight:600}
.model{background:var(--orange);color:var(--white);text-align:center}
.spec{display:flex;align-items:center;border-bottom:1px solid #e6e6e6}
.spec .tk{color:var(--orange);font-weight:700}
.rent{color:var(--orange);font-weight:700;text-align:center}
.band-dark{background:linear-gradient(180deg,#2c2c34,#35363e 60%,#2a2a2e)}
.why-item{color:var(--white)}
.why-item p{color:#c8c8c8}
.helmet{background:radial-gradient(circle at 50% 45%,#6b5a3a 0%,#a89668 40%,#ececec 72%)}
.footer{background:var(--dark);color:var(--white)}
.social{display:flex;gap:7px}
.social span{width:15px;height:15px;background:var(--orange);display:block}
</style>
</head>
<body>

<!-- Desktop view -->
<main class="page page-desktop">
  <section class="a hero" style="left:0;top:0;width:565px;height:312px" role="img" aria-label="Photo of rental scooters parked in a row"></section>
  <div class="a hero-shade" style="left:0;top:0;width:565px;height:312px"></div>

  <header class="a navbar" style="left:45px;top:14px;width:487px;height:50px;padding:0 10px">
    <div class="brand" style="font-size:13px;width:120px"><span class="brand-dot" style="width:10px;height:10px"></span>RIDE ON</div>
    <nav class="nav-links" style="gap:19px;font-size:9.5px;margin-left:16px">
      <span>Reservation</span><span>Prices</span><span>Terms</span><span>FAQ</span><span>Contact</span>
    </nav>
    <div class="phone-badge" style="width:19px;height:19px;margin-left:21px">
      <svg width="10" height="10" viewBox="0 0 24 24"><path fill="#fff" d="M6.6 10.8a15 15 0 006.6 6.6l2.2-2.2c.3-.3.7-.4 1-.2 1.1.4 2.3.6 3.6.6.6 0 1 .4 1 1V20c0 .6-.4 1-1 1A17 17 0 013 4c0-.6.4-1 1-1h3.5c.6 0 1 .4 1 1 0 1.3.2 2.5.6 3.6.1.3 0 .7-.2 1z"/></svg>
    </div>
    <span style="font-size:9px;margin-left:5px">+66 0700 555 210</span>
  </header>

  <h1 class="a hero-title" style="left:40px;top:104px;width:485px;font-size:35px">Fast Motorbike Rentals In<br>Phuket, Thailand</h1>
  <a class="a btn-orange" style="left:209px;top:209px;width:153px;height:45px;font-size:12px;letter-spacing:.3px">Discover Services</a>

  <section class="a booking" style="left:45px;top:268px;width:488px;height:80px">
    <h2 class="a" style="left:7px;top:15px;font-size:11px;font-weight:700">EASY BOOKING</h2>
    <div class="a field" style="left:8px;top:38px;width:91px;height:21px;font-size:6.5px;padding-left:3px">Pick -Up</div>
    <div class="a field" style="left:103px;top:38px;width:91px;height:21px;font-size:6.5px;padding-left:3px">Drop - Off</div>
    <div class="a field" style="left:198px;top:38px;width:91px;height:21px;font-size:6px;padding-left:4px;gap:3px"><span class="flag" style="width:10px;height:7px"></span><span style="color:#333">+66</span> 0700 555 210</div>
    <div class="a field" style="left:293px;top:38px;width:91px;height:21px;font-size:6.5px;padding-left:3px;color:#333">Choose Motorbike<span style="margin-left:auto;margin-right:5px;font-size:5px">▼</span></div>
    <a class="a btn-black" style="left:389px;top:37px;width:91px;height:21px;font-size:9px">Quick Request →</a>
  </section>

  <div class="a sec-icon" style="left:246px;top:366px;width:82px;height:22px;gap:3px"><span class="line" style="width:27px"></span><span class="dot" style="width:22px;height:22px"></span><span class="line" style="width:27px"></span></div>
  <h2 class="a heading" style="left:0;top:392px;width:573px;font-size:26px">How It Works</h2>

  <div class="a illus" style="left:3px;top:443px;width:157px;height:106px" role="img" aria-label="Illustration of an orange motorbike"></div>
  <div class="a step" style="left:171px;top:440px;width:116px;height:116px;background:var(--card-grey)"><p class="a" style="left:6px;top:10px;font-size:10.5px;color:#555;line-height:1.25">Choose<br>Your Bike</p><span class="step-num" style="font-size:48px">1</span></div>
  <div class="a step" style="left:294px;top:440px;width:115px;height:116px;background:var(--card-peach)"><p class="a" style="left:6px;top:10px;font-size:10.5px;color:#555;line-height:1.25">Enter Rental Date<br>Period &amp; Enter<br>Delivery Address Or<br>Choose To Pick Up</p><span class="step-num" style="font-size:48px">2</span></div>
  <div class="a step" style="left:416px;top:440px;width:116px;height:116px;background:var(--card-mint)"><p class="a" style="left:6px;top:10px;font-size:10.5px;color:#555;line-height:1.25">Get Your Bike<br>Delivered In Less<br>Than 2 Hours Or<br>Pick Up ASAP!</p><span class="step-num" style="font-size:48px">3</span></div>

  <a class="a btn-black" style="left:242px;top:582px;width:106px;height:21px;font-size:9.5px">Start Your Search →</a>
  <div class="a" style="left:0;top:626px;width:565px;height:1px;background:#e2e2e2"></div>

  <h2 class="a" style="left:45px;top:656px;font-size:19px;font-weight:600;line-height:1.2">Fast Motorbike Rentals<br>In Phuket, Thailand</h2>
  <div class="a photo-a" style="left:0;top:716px;width:256px;height:159px" role="img" aria-label="Photo of tourists on a scooter"></div>
  <div class="a photo-b" style="left:272px;top:657px;width:209px;height:115px" role="img" aria-label="Photo of a Phuket street with traffic"></div>
  <div class="a photo-c" style="left:494px;top:657px;width:71px;height:115px" role="img" aria-label="Photo of shop fronts in Phuket"></div>
  <h3 class="a" style="left:272px;top:779px;font-size:16px;font-weight:600">Renting Service Features</h3>
  <ul class="a features" style="left:272px;top:801px;font-size:7px;line-height:11px;color:#333">
    <li><span class="tick-box" style="width:5px;height:5px;margin-right:5px"></span>Free Delivery &amp; Pick Up Anywhere In Phuket</li>
    <li><span class="tick-box" style="width:5px;height:5px;margin-right:5px"></span>Free High Quality Helmet Included</li>
    <li><span class="tick-box" style="width:5px;height:5px;margin-right:5px"></span>Free Unlimited Mileage</li>
    <li><span class="tick-box" style="width:5px;height:5px;margin-right:5px"></span>Easy &amp; Quick Online Booking</li>
    <li><span class="tick-box" style="width:5px;height:5px;margin-right:5px"></span>No Credit Card Required</li>
    <li><span class="tick-box" style="width:5px;height:5px;margin-right:5px"></span>Pay When Bike Is Delivered</li>
    <li><span class="tick-box" style="width:5px;height:5px;margin-right:5px"></span>Speak English &amp; Thai</li>
  </ul>

  <section class="a band-orange" style="left:0;top:913px;width:565px;height:237px"></section>
  <h2 class="a heading" style="left:0;top:943px;width:573px;font-size:26px;color:var(--white)">Choose Your Bike</h2>

  <article class="a bike-card" style="left:45px;top:1000px;width:155px;height:200px">
    <div class="a bike-photo" style="left:15px;top:2px;width:125px;height:100px" role="img" aria-label="Photo of a grey scooter"></div>
    <p class="a price" style="left:0;top:105px;width:155px;font-size:12px">200 Baht/Day</p>
    <p class="a model" style="left:29px;top:123px;width:97px;height:17px;font-size:10px;line-height:18px">Breeze 125</p>
    <div class="a spec" style="left:2px;top:155px;width:153px;height:21px;font-size:6.5px"><span class="tk" style="width:12px">✓</span><span style="width:68px">Transmission</span>Automatic</div>
    <div class="a spec" style="left:2px;top:177px;width:153px;height:21px;font-size:6.5px"><span class="tk" style="width:12px">✓</span><span style="width:68px">Engine Capacity</span>150 cc</div>
  </article>
  <article class="a bike-card" style="left:211px;top:1000px;width:155px;height:200px">
    <div class="a bike-photo blue" style="left:15px;top:2px;width:125px;height:100px" role="img" aria-label="Photo of a blue scooter"></div>
    <p class="a price" style="left:0;top:105px;width:155px;font-size:12px">225 Baht/Day</p>
    <p class="a model" style="left:29px;top:123px;width:97px;height:17px;font-size:10px;line-height:18px">Coast 160</p>
    <div class="a spec" style="left:2px;top:155px;width:153px;height:21px;font-size:6.5px"><span class="tk" style="width:12px">✓</span><span style="width:68px">Transmission</span>Automatic</div>
    <div class="a spec" style="left:2px;top:177px;width:153px;height:21px;font-size:6.5px"><span class="tk" style="width:12px">✓</span><span style="width:68px">Engine Capacity</span>153cc</div>
  </article>
  <article class="a bike-card" style="left:377px;top:1000px;width:155px;height:200px">
    <div class="a bike-photo black" style="left:15px;top:4px;width:125px;height:100px" role="img" aria-label="Photo of a black maxi scooter"></div>
    <p class="a price" style="left:0;top:107px;width:155px;font-size:12px">400 Baht/Day</p>
    <p class="a model" style="left:29px;top:125px;width:97px;height:17px;font-size:10px;line-height:18px">Summit 300</p>
    <div class="a spec" style="left:2px;top:155px;width:153px;height:21px;font-size:6.5px"><span class="tk" style="width:12px">✓</span><span style="width:68px">Transmission</span>Automatic</div>
    <div class="a spec" style="left:2px;top:177px;width:153px;height:21px;font-size:6.5px"><span class="tk" style="width:12px">✓</span><span style="width:68px">Engine Capacity</span>279 cc</div>
  </article>
</main>

<!-- Full page view -->
<main class="page page-full">
  <section class="a hero" style="left:0;top:0;width:292px;height:158px" role="img" aria-label="Photo of rental scooters parked in a row"></section>
  <div class="a hero-shade" style="left:0;top:0;width:292px;height:158px"></div>
  <header class="a navbar" style="left:24px;top:8px;width:246px;height:24px;padding:0 5px">
    <div class="brand" style="font-size:7px;width:62px"><span class="brand-dot" style="width:5px;height:5px"></span>RIDE ON</div>
    <nav class="nav-links" style="gap:8px;font-size:4.3px;margin-left:7px"><span>Reservation</span><span>Prices</span><span>Terms</span><span>FAQ</span><span>Contact</span></nav>
    <span class="phone-badge" style="width:9px;height:9px;margin-left:8px"></span>
    <span style="font-size:4.2px;margin-left:3px">+66 0700 555 210</span>
  </header>
  <h1 class="a hero-title" style="left:10px;top:52px;width:272px;font-size:18px">Fast Motorbike Rentals In<br>Phuket, Thailand</h1>
  <a class="a btn-orange" style="left:106px;top:105px;width:78px;height:23px;font-size:6px">Discover Services</a>

  <section class="a booking" style="left:24px;top:136px;width:246px;height:40px">
    <h2 class="a" style="left:3px;top:8px;font-size:5.5px;font-weight:700">EASY BOOKING</h2>
    <div class="a field" style="left:4px;top:19px;width:46px;height:10px;font-size:3.2px;padding-left:2px">Pick -Up</div>
    <div class="a field" style="left:53px;top:19px;width:46px;height:10px;font-size:3.2px;padding-left:2px">Drop - Off</div>
    <div class="a field" style="left:101px;top:19px;width:46px;height:10px;font-size:3px;padding-left:2px;gap:1px"><span class="flag" style="width:5px;height:4px"></span>+66 0700 555 210</div>
    <div class="a field" style="left:149px;top:19px;width:46px;height:10px;font-size:3.2px;padding-left:2px;color:#333">Choose Motorbike</div>
    <a class="a btn-black" style="left:198px;top:18px;width:45px;height:11px;font-size:4.5px">Quick Request →</a>
  </section>

  <div class="a sec-icon" style="left:125px;top:184px;width:42px;height:11px;gap:2px"><span class="line" style="width:14px"></span><span class="dot" style="width:11px;height:11px"></span><span class="line" style="width:14px"></span></div>
  <h2 class="a heading" style="left:0;top:199px;width:292px;font-size:13px">How It Works</h2>
  <div class="a illus" style="left:2px;top:224px;width:78px;height:54px" role="img" aria-label="Illustration of an orange motorbike"></div>
  <div class="a step" style="left:87px;top:223px;width:58px;height:59px;background:var(--card-grey)"><p class="a" style="left:3px;top:5px;font-size:5px;color:#555;line-height:1.25">Choose<br>Your Bike</p><span class="step-num" style="font-size:24px">1</span></div>
  <div class="a step" style="left:149px;top:223px;width:58px;height:59px;background:var(--card-peach)"><p class="a" style="left:3px;top:5px;font-size:5px;color:#555;line-height:1.25">Enter Rental Date<br>Period &amp; Enter<br>Delivery Address Or<br>Choose To Pick Up</p><span class="step-num" style="font-size:24px">2</span></div>
  <div class="a step" style="left:212px;top:223px;width:58px;height:59px;background:var(--card-mint)"><p class="a" style="left:3px;top:5px;font-size:5px;color:#555;line-height:1.25">Get Your Bike<br>Delivered In Less<br>Than 2 Hours Or<br>Pick Up ASAP!</p><span class="step-num" style="font-size:24px">3</span></div>
  <a class="a btn-black" style="left:123px;top:295px;width:54px;height:10px;font-size:4.6px">Start Your Search →</a>
  <div class="a" style="left:0;top:317px;width:292px;height:1px;background:#e6e6e6"></div>

  <h2 class="a" style="left:24px;top:333px;font-size:9.5px;font-weight:600;line-height:1.2">Fast Motorbike Rentals<br>In Phuket, Thailand</h2>
  <div class="a photo-a" style="left:1px;top:363px;width:130px;height:80px" role="img" aria-label="Photo of tourists on a scooter"></div>
  <div class="a photo-b" style="left:139px;top:333px;width:106px;height:59px" role="img" aria-label="Photo of a Phuket street with traffic"></div>
  <div class="a photo-c" style="left:251px;top:333px;width:41px;height:59px" role="img" aria-label="Photo of shop fronts in Phuket"></div>
  <h3 class="a" style="left:138px;top:395px;font-size:8px;font-weight:600">Renting Service Features</h3>
  <ul class="a features" style="left:138px;top:406px;font-size:3.3px;line-height:5.6px;color:#333">
    <li><span class="tick-box" style="width:3px;height:3px;margin-right:3px"></span>Free Delivery &amp; Pick Up Anywhere In Phuket</li>
    <li><span class="tick-box" style="width:3px;height:3px;margin-right:3px"></span>Free High Quality Helmet Included</li>
    <li><span class="tick-box" style="width:3px;height:3px;margin-right:3px"></span>Free Unlimited Mileage</li>
    <li><span class="tick-box" style="width:3px;height:3px;margin-right:3px"></span>Easy &amp; Quick Online Booking</li>
    <li><span class="tick-box" style="width:3px;height:3px;margin-right:3px"></span>No Credit Card Required</li>
    <li><span class="tick-box" style="width:3px;height:3px;margin-right:3px"></span>Pay When Bike Is Delivered</li>
    <li><span class="tick-box" style="width:3px;height:3px;margin-right:3px"></span>Speak English &amp; Thai</li>
  </ul>

  <section class="a band-orange" style="left:0;top:462px;width:292px;height:120px"></section>
  <h2 class="a heading" style="left:0;top:478px;width:292px;font-size:13px;color:var(--white)">Choose Your Bike</h2>

  <article class="a bike-card" style="left:24px;top:507px;width:78px;height:201px;font-size:3px">
    <div class="a bike-photo" style="left:8px;top:1px;width:62px;height:52px" role="img" aria-label="Photo of a grey scooter"></div>
    <p class="a price" style="left:0;top:55px;width:78px;font-size:5.5px">200 Baht/Day</p>
    <p class="a model" style="left:15px;top:63px;width:48px;height:9px;font-size:4.5px;line-height:9.5px">Breeze 125</p>
    <div class="a" style="left:1px;top:81px;width:77px;line-height:10.8px">
      <div class="spec"><span class="tk" style="width:6px">✓</span><span style="width:33px">Transmission</span>Automatic</div>
      <div class="spec"><span class="tk" style="width:6px">✓</span><span style="width:33px">Engine Capacity</span>150 cc</div>
      <div class="spec"><span class="tk" style="width:6px">✓</span><span style="width:33px">Curb weight</span>106 kg (233.7 lbs)</div>
      <div class="spec"><span class="tk" style="width:6px">✓</span><span style="width:33px">Fuel Tank Volume</span>5.5 Liters</div>
      <div class="spec"><span class="tk" style="width:6px">✓</span><span style="width:33px">Range</span>About 200 Km</div>
      <div class="spec"><span class="tk" style="width:6px">✓</span><span style="width:33px">Top Speed</span>120 Km/H</div>
      <div class="spec"><span class="tk" style="width:6px">✓</span><span style="width:33px">Power Output</span>11.40 HP</div>
      <div class="spec"><span class="tk" style="width:6px">✓</span><span style="width:33px">Maximum Torque</span>11.6 Nm</div>
      <div class="spec"><span class="tk" style="width:6px">✓</span><span style="width:33px">Fuel Consumption</span>58.8 km/L</div>
    </div>
    <p class="a rent" style="left:0;top:189px;width:78px;font-size:4.3px">RENT BIKE NOW</p>
  </article>
  <article class="a bike-card" style="left:108px;top:507px;width:78px;height:201px;font-size:3px">
    <div class="a bike-photo blue" style="left:8px;top:1px;width:62px;height:52px" role="img" aria-label="Photo of a blue scooter"></div>
    <p class="a price" style="left:0;top:55px;width:78px;font-size:5.5px">225 Baht/Day</p>
    <p class="a model" style="left:15px;top:63px;width:48px;height:9px;font-size:4.5px;line-height:9.5px">Coast 160</p>
    <div class="a" style="left:1px;top:81px;width:77px;line-height:10.8px">
      <div class="spec"><span class="tk" style="width:6px">✓</span><span style="width:33px">Transmission</span>Automatic</div>
      <div class="spec"><span class="tk" style="width:6px">✓</span><span style="width:33px">Engine Capacity</span>153cc</div>
      <div class="spec"><span class="tk" style="width:6px">✓</span><span style="width:33px">Curb weight</span>106 kg (233.7 lbs)</div>
      <div class="spec"><span class="tk" style="width:6px">✓</span><span style="width:33px">Fuel Tank Volume</span>6.06 Liters</div>
      <div class="spec"><span class="tk" style="width:6px">✓</span><span style="width:33px">Range</span>-</div>
      <div class="spec"><span class="tk" style="width:6px">✓</span><span style="width:33px">Top Speed</span>115 Km/H</div>
      <div class="spec"><span class="tk" style="width:6px">✓</span><span style="width:33px">Power Output</span>13.50 HP</div>
      <div class="spec"><span class="tk" style="width:6px">✓</span><span style="width:33px">Maximum Torque</span>14 Nm</div>
      <div class="spec"><span class="tk" style="width:6px">✓</span><span style="width:33px">Fuel Consumption</span>43.3 km/L</div>
    </div>
    <p class="a rent" style="left:0;top:189px;width:78px;font-size:4.3px">RENT BIKE NOW</p>
  </article>
  <article class="a bike-card" style="left:192px;top:507px;width:78px;height:201px;font-size:3px">
    <div class="a bike-photo black" style="left:8px;top:2px;width:62px;height:52px" role="img" aria-label="Photo of a black maxi scooter"></div>
    <p class="a price" style="left:0;top:56px;width:78px;font-size:5.5px">400 Baht/Day</p>
    <p class="a model" style="left:15px;top:64px;width:48px;height:9px;font-size:4.5px;line-height:9.5px">Summit 300</p>
    <div class="a" style="left:1px;top:81px;width:77px;line-height:10.8px">
      <div class="spec"><span class="tk" style="width:6px">✓</span><span style="width:33px">Transmission</span>Automatic</div>
      <div class="spec"><span class="tk" style="width:6px">✓</span><span style="width:33px">Engine Capacity</span>279 cc</div>
      <div class="spec"><span class="tk" style="width:6px">✓</span><span style="width:33px">Curb weight</span>182 kg (401 lbs)</div>
      <div class="spec"><span class="tk" style="width:6px">✓</span><span style="width:33px">Fuel Tank Volume</span>11.5 Liters</div>
      <div class="spec"><span class="tk" style="width:6px">✓</span><span style="width:33px">Range</span>-</div>
      <div class="spec"><span class="tk" style="width:6px">✓</span><span style="width:33px">Top Speed</span>135 Km/H</div>
      <div class="spec"><span class="tk" style="width:6px">✓</span><span style="width:33px">Power Output</span>24.81 HP</div>
      <div class="spec"><span class="tk" style="width:6px">✓</span><span style="width:33px">Maximum Torque</span>27.2 Nm</div>
      <div class="spec"><span class="tk" style="width:6px">✓</span><span style="width:33px">Fuel Consumption</span>37.0 km/L</div>
    </div>
    <p class="a rent" style="left:0;top:189px;width:78px;font-size:4.3px">RENT BIKE NOW</p>
  </article>
  <div class="a" style="left:140px;top:720px;width:8px;height:8px;background:#000;color:#fff;font-size:6px;text-align:center;line-height:9px">‹</div>
  <div class="a" style="left:151px;top:720px;width:8px;height:8px;background:#000;color:#fff;font-size:6px;text-align:center;line-height:9px">›</div>

  <section class="a band-dark" style="left:0;top:742px;width:292px;height:178px">
    <span class="a" style="left:141px;top:13px;width:10px;height:10px;border-radius:50%;background:var(--orange)"></span>
    <h2 class="a heading" style="left:0;top:30px;width:292px;font-size:12.5px;color:var(--white)">Why Choose RIDE ON</h2>
    <div class="a why-item" style="left:20px;top:63px;width:80px;text-align:right"><h4 style="font-size:6.5px;font-weight:600;line-height:1.2">Fully Insure<br>Rental Service</h4><p style="font-size:3px;margin-top:3px">Short note on full insurance for every rental.</p></div>
    <div class="a why-item" style="left:20px;top:113px;width:80px;text-align:right"><h4 style="font-size:6.5px;font-weight:600;line-height:1.2">Different Types<br>Of Bikes</h4><p style="font-size:3px;margin-top:3px">Short note on the range of bikes offered.</p></div>
    <div class="a why-item" style="left:200px;top:63px;width:80px"><h4 style="font-size:6.5px;font-weight:600;line-height:1.2">Fully Insure<br>Rental Service</h4><p style="font-size:3px;margin-top:3px">Short note on full insurance for every rental.</p></div>
    <div class="a why-item" style="left:200px;top:113px;width:80px"><h4 style="font-size:6.5px;font-weight:600;line-height:1.2">Different Types<br>Of Bikes</h4><p style="font-size:3px;margin-top:3px">Short note on the range of bikes offered.</p></div>
    <div class="a" style="left:101px;top:65px;width:91px;height:91px;border-radius:50%;background:var(--orange);border:3px solid #fff" role="img" aria-label="Illustration of a rider on a motorbike"></div>
  </section>

  <div class="a sec-icon" style="left:125px;top:928px;width:42px;height:10px;gap:2px"><span class="line" style="width:14px"></span><span class="dot" style="width:10px;height:10px"></span><span class="line" style="width:14px"></span></div>
  <h2 class="a heading" style="left:0;top:944px;width:292px;font-size:12.5px">Free Helmets</h2>
  <div class="a helmet" style="left:24px;top:971px;width:55px;height:56px" role="img" aria-label="Photo of an open-face helmet"></div>
  <div class="a helmet" style="left:88px;top:971px;width:55px;height:56px" role="img" aria-label="Photo of an open-face helmet"></div>
  <div class="a helmet" style="left:152px;top:971px;width:55px;height:56px" role="img" aria-label="Photo of an open-face helmet"></div>
  <div class="a helmet" style="left:216px;top:971px;width:55px;height:56px" role="img" aria-label="Photo of an open-face helmet"></div>

  <footer class="a footer" style="left:0;top:1060px;width:292px;height:128px">
    <div class="a" style="left:67px;top:40px;width:160px;text-align:center;font-size:10px">☏ +66 0700 555 210</div>
    <nav class="a nav-links" style="left:0;top:63px;width:292px;justify-content:center;gap:11px;font-size:4.5px"><span>Reservation</span><span>Prices</span><span>Terms</span><span>FAQ</span><span>Contact</span></nav>
    <div class="a social" style="left:106px;top:82px"><span></span><span></span><span></span><span></span></div>
    <p class="a" style="left:0;top:112px;width:292px;text-align:center;font-size:3.4px">Copyright RIDE ON 2021. All right reserved.</p>
  </footer>
  <div class="a band-orange" style="left:24px;top:1042px;width:246px;height:43px;border-bottom:2px solid #fff"><h2 style="color:#fff;text-align:center;font-size:12.5px;font-weight:600;line-height:1.2;margin-top:6px">Fast Motorbike Rentals In<br>Phuket, Thailand</h2></div>
</main>

</body>
</html>
```